Real Estate 2015 sold listings postcard

Real estate. I want one side to list 2015 sales. Mailing side with additional information. I am including a "concept" but it needs to be professionalized... Feel free to change color, fonts, layout, add watermark, whatever you think will work. Text on backside may be tweaked. I do want postcards addressed. How do i send mailing list or does Quorra Mail do that part?

NOTE: Postcard should be 8.5 x 5.5 inches.

postcard should be 8.5" x 5.5" size

Target Market(s)

Home owners who may want to sell

Industry/Entity Type

Real Estate Agent

Requirements
Must have
• The sold information and contact oinformation I have provided
Nice to have
• Watermark with my initials

```html
<!DOCTYPE html>
<html lang="en">
<head>
<meta charset="utf-8">
<title>Best Months to Sell – Postcard</title>
<link href="https://fonts.googleapis.com/css2?family=Lato:wght@300;400;700;900&display=swap" rel="stylesheet">
<style>
  :root{
    --red:#e3313a;
    --red-deep:#b8232a;
    --red-dark:#8f1f22;
    --maroon:#a4282b;
    --gold:#d9a406;
    --ink:#2b2b2b;
    --paper:#ffffff;
    --mist:#e6e6e6;
  }
  *{margin:0;padding:0;box-sizing:border-box}
  html,body{width:1200px;height:773px;overflow:hidden;background:var(--paper)}
  .postcard{
    position:relative;width:1200px;height:773px;overflow:hidden;
    font-family:'Lato',sans-serif;color:var(--ink);
    background:linear-gradient(90deg,var(--mist) 0%,#f7f7f7 40%,var(--paper) 60%);
    border:1px solid #9a9a9a;
  }
  .wave{position:absolute;left:0;top:0;width:1200px;height:773px}
  .headline{position:absolute;left:40px;top:22px;color:#fff;line-height:1}
  .headline .lead{font-weight:300;font-size:52px;display:block;margin-bottom:10px}
  .headline .line{font-weight:300;font-size:42px;display:block;margin-bottom:12px}
  .headline b{font-weight:900}
  .tab-offers{
    position:absolute;left:150px;top:212px;width:180px;text-align:center;
    font-weight:900;font-size:33px;color:var(--maroon);letter-spacing:-.3px
  }
  .tab-prices{
    position:absolute;left:44px;top:272px;width:276px;height:57px;
    background:var(--red-deep);border-radius:0 0 22px 22px;
    color:#fff;font-weight:900;font-size:33px;text-align:center;line-height:60px;letter-spacing:-.3px
  }
  .reach{
    position:absolute;right:636px;top:262px;text-align:right;
    font-size:22.5px;line-height:28px;color:var(--maroon)
  }
  .dont-wait{
    position:absolute;left:76px;top:340px;font-weight:300;font-size:39px;color:var(--maroon)
  }
  .cta{position:absolute;left:0;top:369px}
  .cta-text{
    position:absolute;left:32px;top:24px;white-space:nowrap;
    color:#fff;font-weight:900;font-size:27.5px;letter-spacing:-.2px
  }
  .copy{position:absolute;left:22px;top:443px;width:487px;font-size:17.6px;line-height:23.5px;text-align:justify}
  .copy p+p{margin-top:5px}
  .portrait{
    position:absolute;left:650px;top:34px;width:156px;height:156px;border-radius:50%;
    border:2px solid #fff;box-shadow:0 1px 4px rgba(0,0,0,.35);
    background:radial-gradient(circle at 50% 40%,#c99a7c 0 22%,#2f4b48 23% 55%,#c4283a 56%)
  }
  .contact{position:absolute;left:626px;top:192px;width:204px;text-align:center}
  .contact .name{font-weight:900;font-size:21px;color:var(--maroon)}
  .contact .license{font-weight:300;font-size:16px;margin-top:2px;padding-bottom:3px;border-bottom:1px solid #555}
  .contact .phone{font-weight:300;font-size:27px;color:var(--maroon);padding:2px 0 0;border-bottom:1px solid #555;line-height:30px}
  .contact .email{font-size:18px;margin-top:3px}
  .contact .web{
    display:block;margin:3px auto 0;width:176px;height:21px;border-radius:11px;background:var(--gold);
    color:#fff;font-weight:700;font-size:16.5px;line-height:22px
  }
</style>
</head>
<body>
<div class="postcard">
  <svg class="wave" viewBox="0 0 1200 773" aria-hidden="true">
    <defs>
      <linearGradient id="redFill" x1="0" y1="0" x2="1" y2="0">
        <stop offset="0" stop-color="#d92a33"/>
        <stop offset=".45" stop-color="#e8414a"/>
        <stop offset="1" stop-color="#c8262c"/>
      </linearGradient>
    </defs>
    <path d="M0 0H1200V118C1080 92 940 98 810 124C660 160 520 235 300 262C180 276 70 245 0 206Z" fill="var(--red-dark)"/>
    <path d="M0 0H1200V66C1060 70 920 98 800 142C650 205 520 248 300 254C170 258 70 232 0 200Z" fill="url(#redFill)"/>
    <path d="M94 238C112 214 122 196 150 196H325C352 196 360 216 376 236C330 250 290 256 240 258C180 258 130 250 94 238Z" fill="#fff"/>
  </svg>

  <h1 class="headline">
    <span class="lead">Traditionally</span>
    <span class="line"><b>FEB</b> through <b>APRIL</b></span>
    <span class="line">are the <b>best months to sell</b></span>
  </h1>

  <div class="tab-offers">Most Offers</div>
  <div class="tab-prices">Highest Prices</div>

  <p class="reach">Our Listings are<br>advertised Locally and<br>in 40 countries!!</p>

  <p class="dont-wait">Don't Wait...</p>

  <div class="cta">
    <svg width="525" height="64" viewBox="0 0 525 64" aria-hidden="true">
      <polygon points="465,1 522,1 497,33 522,64 490,64 490,18" fill="#c99505"/>
      <polygon points="465,1 490,18 490,13" fill="#8a6603"/>
      <rect x="0" y="17" width="490" height="47" fill="var(--gold)"/>
    </svg>
    <span class="cta-text">Call Now for a Private Consultation!</span>
  </div>

  <div class="copy">
    <p>Our market continues to be strong, which reflects both our vibrant and growing local economy and our seemingly chronic shortage of inventory. As long as those conditions continue, our market values will remain high. That is good news to sellers who may want to down-size or move to a different area for a new job, or maybe to be closer to family.</p>
    <p>I am an Brookline Crest Realtors certified Relocation Specialist, and, as such, I can connect you with experienced and professional real estate agent anywhere in the country and in most countries around the world. We can co-ordinate your transactions at both ends, making your transition as seamless as possible. If you are planning a move, across the street or across the county, call me now for a confidential consultation.</p>
  </div>

  <div class="portrait" role="img" aria-label="Portrait photo of the agent, Delia Hartwell"></div>

  <div class="contact">
    <div class="name">DELIA HARTWELL</div>
    <div class="license">License : #00482137</div>
    <div class="phone">650-555-0148</div>
    <div class="email">Dhartwell@bcr.com</div>
    <span class="web">www.Dhartwell.com</span>
  </div>
</div>
</body>
</html>
```